Zarvo! Next Steps?, Bail Bond Company Check-in App , Court date, Court Reminders, Payments

Zarvo!
Next Steps?
WINNER OF THIS CONTEST WILL HAVE OPPORTUNITY TO DESIGN CUSTOMIZE SOME OUR COMPANY PAGES AFTER CONTEST!
Check-in with your Bail agent via pic/video
Receive Court reminders
Make a payments

Basically this app is a portal to 3rd party bail companies.
The idea is for the person whom makes bail downloads the Zarvo app from App Store.
Then they select a bail bond company.
This would be similar to a restaurant, real estate agent, insurance agent,,app where we could populate bail bond companies by client location or by typing in name of bail company.
We would like the ability to customize each bail bond company landing pages but are open to a global concept. when you click the bail bond company location it would have the logos for that company so the bail bond company screens would need to be customizeble
The app will require a photo or video check-in that is date and time
stamped with a gps location stored in check-in history
Check-in can be scheduled or random or voluntary
Voluntary and Scheduled Check-ins would require check-in button
Random would be via alert or text

The app should be able to receive court date updates
The app should allow clients to make payments to bail bond company
we need
ZARVO! landing page
client registration screens, check-in screens, available bail bond company screens for client to choose from
client registration page should include
name
email address
phone number
picture
home address
work address
date of birth
this app is different from our u-trak app. this is a bail bond check-in app for third party bail bond companies.
landing page should be ZARVO! Next Steps?
ZARVO ! Registration
Find your bail bond Company should list bail bond companies near me and search bar for searching bail bond companies by name
Next landing pages would be customizable for the third party bail bond companies
these would include pages for
check-ins via pics/videos
payment page
court reminders
contact information for bail bond companies
Zarvo Pages include
initial landing page
registration page
search bail companies

Bail bond company pages should include
Bali bond company landing page
Use KELNOR BAIL BOND COMPANY as example
contact information for bail company
check-in page
payment page
court reminder page
Updates

Low designer entries

Low designer entries

Sick

Sick

Sick

Target Market(s)

Court Defendants, Probation ,jails, sheriffs, judges, attorneys

Industry/Entity Type

justice, law enforcement, courts,

Requirements
Must have
• Check-in via pic/video, ability to receive court date reminders, make paymentswe need client registration screens, check-in screens, available bail bond company screens for client to choose from
Nice to have
• Professional easy to navigate intuitive customizable to 3rd party bail bond companies, logos,phone numbers etc.
Should not have
• unprofessional graphics,

```html
<!DOCTYPE html>
<html lang="en">
<head>
<meta charset="utf-8">
<title>Zarvo! Next Steps? – Bail Agent App Screens</title>
<link href="https://fonts.googleapis.com/css2?family=Poppins:wght@400;500;600;700&display=swap" rel="stylesheet">
<style>
:root{
  --canvas:#d9d9d9;
  --ink:#2b2b2b;
  --ink-soft:#3a3a3a;
  --paper:#ffffff;
  --paper-soft:#fafafa;
  --muted:#8a8a8a;
  --alert:#ef3b3b;
  --star:#8fa33a;
  --logo-box:#e5e5e5;
}
*{box-sizing:border-box;margin:0;padding:0}
html,body{width:1200px;height:953px;overflow:hidden;background:var(--canvas);font-family:"Poppins",sans-serif;color:var(--ink)}
.stage{position:absolute;left:0;top:0;width:1490px;height:1183px;transform:scale(0.80537);transform-origin:0 0}
.abs{position:absolute}
.screen{position:absolute;background:var(--paper-soft);overflow:hidden}
.screen--home{left:268px;top:116px;width:375px;height:812px}
.screen--company{left:822px;top:116px;width:375px;height:919px;background:var(--paper)}
.topbar{position:absolute;left:0;top:0;width:375px;height:124px;background:var(--ink)}
.location{left:32px;top:20px;display:flex;align-items:center;gap:10px;color:var(--paper);font-size:16px}
.search{left:31px;top:66px;width:262px;height:37px;background:var(--paper);border-radius:6px;display:flex;align-items:center;padding-left:14px;gap:18px;font-size:12px;color:#9a9a9a}
.filter{left:324px;top:66px;width:34px;height:36px;background:var(--paper);border-radius:4px}
.promo{left:10px;top:135px;width:355px;height:150px;background:var(--ink);border-radius:14px}
.photo{position:absolute;border-radius:10px}
.photo--promo{left:27px;top:16px;width:136px;height:108px;background:linear-gradient(135deg,#c9cbe0,#8d92c7 60%,#b7b9cf)}
.photo-name{position:absolute;inset:0;display:flex;align-items:center;justify-content:center;font-weight:600;color:#b3231f;font-size:20px}
.promo-title{left:172px;top:28px;width:170px;color:var(--paper);font-weight:600;font-size:17px;line-height:22px}
.btn-light{left:177px;top:92px;width:111px;height:29px;background:var(--paper);border-radius:3px;font-size:10px;display:flex;align-items:center;justify-content:center}
.section-title{left:31px;top:310px;font-size:15px;font-weight:500}
.agent{position:absolute;background:var(--paper);border-radius:16px;box-shadow:0 6px 18px rgba(0,0,0,.05);text-align:center}
.agent-logo{margin:23px auto 0;width:96px;height:73px;background:var(--logo-box);display:flex;align-items:center;justify-content:center;gap:5px;font-size:10px;font-weight:600}
.agent-logo--plain{background:none}
.agent-logo i{width:8px;height:8px;background:#d8291c;display:block}
.agent-logo--plain i{background:#f28a12;border-radius:50%}
.agent-name{margin-top:14px;font-size:14px}
.agent-rating{margin-top:12px;font-size:12px;color:var(--muted)}
.agent-rating b{color:var(--star);font-weight:400;margin-right:6px;font-size:10px}
.navbar{left:10px;top:728px;width:355px;height:74px;background:var(--ink);border-radius:22px}
.nav-home{left:20px;top:15px;width:105px;height:44px;background:var(--ink-soft);border-radius:10px;display:flex;align-items:center;gap:10px;padding-left:18px;color:var(--paper);font-size:13px}
.company-head-title{left:130px;top:46px;width:210px;color:var(--paper);font-size:15px;font-weight:600;line-height:20px}
.photo--head{left:23px;top:33px;width:91px;height:72px;background:linear-gradient(135deg,#c9cbe0,#9297c8 60%,#b7b9cf)}
.photo--head .photo-name{font-size:14px}
.headline{left:33px;top:136px;width:320px;font-size:16px;font-weight:500;line-height:24px}
.why{left:0;top:191px;width:375px;height:192px;background:linear-gradient(120deg,#2f2b29 0%,#4a3a33 40%,#6b4c3c 55%,#3b3634 75%,#555 100%)}
.why-title{left:36px;top:12px;color:var(--paper);font-weight:600;font-size:15px}
.why-list{left:36px;top:40px;list-style:none;color:var(--paper);font-size:10px}
.why-list li{height:28px}
.services-title{left:0;top:399px;width:375px;text-align:center;font-size:12px;font-weight:500}
.service{position:absolute;width:149px;background:var(--paper);border-radius:16px;box-shadow:0 6px 18px rgba(0,0,0,.06);text-align:center;font-size:12px;font-weight:500}
.service-art{margin:12px auto 0;width:74px;height:74px;border-radius:50%}
.service-label{margin-top:20px}
.service--last .service-label{margin-top:12px;color:#8f8f8f}
.fade{left:0;top:826px;width:375px;height:93px;background:linear-gradient(rgba(255,255,255,.45),rgba(255,255,255,.9) 45%,#fff 70%)}
.btn-dark{left:96px;top:852px;width:184px;height:48px;background:var(--ink);border-radius:4px;color:var(--paper);font-size:10px;font-weight:500;display:flex;align-items:center;justify-content:center}
</style>
</head>
<body>
<div class="stage">

  <section class="screen screen--home">
    <header class="topbar">
      <div class="abs location">
        <svg width="18" height="20" viewBox="0 0 18 20" fill="none" stroke="#fff" stroke-width="1.8"><path d="M9 19s7-6.5 7-11A7 7 0 0 0 2 8c0 4.5 7 11 7 11z"/><circle cx="9" cy="8" r="2.4"/></svg>
        418 Linden Row, NYC
      </div>
      <svg class="abs" style="left:324px;top:22px" width="24" height="26" viewBox="0 0 24 26" fill="none" stroke="#fff" stroke-width="1.8"><path d="M5 18V11a7 7 0 0 1 14 0v7l2 2H3z"/><path d="M9.5 22a2.5 2.5 0 0 0 5 0"/><circle cx="18" cy="4" r="3.5" fill="#ef3b3b" stroke="none"/></svg>
      <div class="abs search">
        <svg width="17" height="17" viewBox="0 0 17 17" fill="none" stroke="#2b2b2b" stroke-width="2"><circle cx="7" cy="7" r="5.5"/><path d="M11 11l5 5"/></svg>
        What kind of Bail you want?
      </div>
      <div class="abs filter">
        <svg width="34" height="36" viewBox="0 0 34 36"><circle cx="11" cy="13" r="3" fill="#2b2b2b"/><rect x="16" y="12" width="9" height="2" fill="#2b2b2b"/><rect x="8" y="22" width="9" height="2" fill="#2b2b2b"/><circle cx="23" cy="23" r="3" fill="#2b2b2b"/></svg>
      </div>
    </header>

    <article class="abs promo">
      <div class="photo photo--promo" role="img" aria-label="Promotional photo for Harlow Bail"><span class="photo-name">Harlow</span></div>
      <h2 class="abs promo-title">Special Deal From Harlow Bail</h2>
      <div class="abs btn-light">See Details</div>
    </article>

    <h3 class="abs section-title">Available Agent</h3>

    <div class="agent" style="left:30px;top:342px;width:145px;height:180px">
      <div class="agent-logo"><i></i>Veyra Bail</div>
      <p class="agent-name">Bail Agent 1</p>
      <p class="agent-rating"><b>★</b>4.8</p>
    </div>
    <div class="agent" style="left:199px;top:342px;width:133px;height:178px">
      <div class="agent-logo agent-logo--plain"><i></i>Ostrel Bail</div>
      <p class="agent-name" style="margin-top:12px">Bail Agent 2</p>
      <p class="agent-rating"><b>★</b>4.8</p>
    </div>
    <div class="agent" style="left:28px;top:545px;width:145px;height:179px">
      <div class="agent-logo"><i></i>Veyra Bail</div>
      <p class="agent-name">Bail Agent 1</p>
      <p class="agent-rating"><b>★</b>4.8</p>
    </div>
    <div class="agent" style="left:199px;top:545px;width:145px;height:179px">
      <div class="agent-logo"><i></i>Veyra Bail</div>
      <p class="agent-name">Bail Agent 1</p>
      <p class="agent-rating"><b>★</b>4.8</p>
    </div>

    <nav class="abs navbar">
      <div class="abs nav-home">
        <svg width="20" height="20" viewBox="0 0 20 20"><path d="M2 9l8-7 8 7v9h-5v-5H7v5H2z" fill="#fff"/></svg>
        Home
      </div>
      <svg class="abs" style="left:169px;top:26px" width="18" height="22" viewBox="0 0 18 22" fill="#8a8a8a"><circle cx="9" cy="5.5" r="5"/><path d="M0 22a9 7 0 0 1 18 0z"/></svg>
      <svg class="abs" style="left:226px;top:22px" width="30" height="28" viewBox="0 0 30 28"><path d="M12 6a10 9 0 1 1-6 16l-5 2 2-5A10 9 0 0 1 12 6z" fill="#5a5a5a"/><circle cx="21" cy="7" r="5" fill="#ef3b3b"/></svg>
      <svg class="abs" style="left:302px;top:22px" width="24" height="28" viewBox="0 0 24 28" fill="none" stroke="#fff" stroke-width="1.8"><path d="M5 20V13a7 7 0 0 1 14 0v7l2 2H3z"/><path d="M9.5 24a2.5 2.5 0 0 0 5 0"/><circle cx="19" cy="6" r="3.5" fill="#ef3b3b" stroke="none"/></svg>
    </nav>
  </section>

  <section class="screen screen--company">
    <header class="topbar">
      <div class="photo photo--head" role="img" aria-label="Harlow Bail company photo"><span class="photo-name">Harlow</span></div>
      <h2 class="abs company-head-title">Special Deal From Harlow Bail</h2>
      <svg class="abs" style="left:249px;top:89px" width="16" height="16" viewBox="0 0 16 16"><path d="M3 1l3 3-1.5 2a9 9 0 0 0 5.5 5.5L12 10l3 3-2 2C6 15 1 9 1 3z" fill="#fff"/></svg>
      <svg class="abs" style="left:281px;top:90px" width="16" height="13" viewBox="0 0 16 13"><rect width="16" height="13" rx="1.5" fill="#fff"/><path d="M1 2l7 5 7-5" fill="none" stroke="#2b2b2b" stroke-width="1.5"/></svg>
      <svg class="abs" style="left:313px;top:88px" width="14" height="18" viewBox="0 0 14 18"><path d="M7 17s6-6 6-10A6 6 0 0 0 1 7c0 4 6 10 6 10z" fill="#fff"/><circle cx="7" cy="7" r="2.2" fill="#2b2b2b"/></svg>
    </header>

    <h1 class="abs headline">Around-the-Clock Bail Bonds from a Reliable Bail Agency in Marlow Bay, ID</h1>

    <div class="abs why" role="img" aria-label="Photo of hands signing bail paperwork at a desk">
      <h3 class="abs why-title">Why Us:</h3>
      <ul class="abs why-list">
        <li>***Amet minim mollit non deserunt ullamco est sit aliqua</li>
        <li>***Amet minim mollit non deserunt ullamco est sit aliqua</li>
        <li>***Amet minim mollit non deserunt ullamco est sit aliqua</li>
        <li>***Amet minim mollit non deserunt ullamco est sit aliqua</li>
        <li>***Amet minim mollit non deserunt ullamco est sit aliqua</li>
      </ul>
    </div>

    <h3 class="abs services-title">Our Services</h3>

    <div class="service" style="left:29px;top:424px;height:137px">
      <div class="service-art" role="img" aria-label="Illustration of hands exchanging cash" style="background:linear-gradient(135deg,#5fc3b8,#3aa99e)"></div>
      <p class="service-label">Cash Bail</p>
    </div>
    <div class="service" style="left:196px;top:424px;height:135px">
      <div class="service-art" role="img" aria-label="Illustration of an agent holding a small house" style="background:linear-gradient(135deg,#cfe0f5,#2b2b2b)"></div>
      <p class="service-label" style="margin-top:18px">Property Bond</p>
    </div>
    <div class="service" style="left:29px;top:582px;height:133px">
      <div class="service-art" role="img" aria-label="Surety bond badge illustration" style="background:radial-gradient(circle,#e4ecf6,#a9c1dd)"></div>
      <p class="service-label">Surety Bond</p>
    </div>
    <div class="service" style="left:196px;top:580px;height:131px">
      <svg class="service-art" style="border-radius:0" viewBox="0 0 74 74" fill="none" stroke="#1a1a1a" stroke-width="2.4"><path d="M37 6a30 27 0 1 1-14 51l-10 4 4-10A30 27 0 0 1 37 6z"/><path d="M24 30c0-4 6-6 8-2 2 5-3 10-7 11M42 30c0-4 6-6 8-2 2 5-3 10-7 11" stroke-width="3.2"/></svg>
      <p class="service-label" style="margin-top:16px">Citation Bond</p>
    </div>
    <div class="service service--last" style="left:29px;top:736px;height:150px">
      <div class="service-art" role="img" aria-label="Illustration of hands in handcuffs holding money" style="background:radial-gradient(circle,#f4ef8a,#c8c8c8)"></div>
      <p class="service-label">Immigration Bail</p>
    </div>
    <div class="service service--last" style="left:196px;top:736px;height:150px">
      <div class="service-art" role="img" aria-label="Sketch of a judge and a defendant at court" style="background:radial-gradient(circle,#f0f0f0,#c9c9c9)"></div>
      <p class="service-label">Personal Recognizance</p>
    </div>

    <div class="abs fade"></div>
    <div class="abs btn-dark">Apply Online</div>
  </section>

</div>
</body>
</html>
```